The Notebook Beneath the Lantern - Book cover design

Book Cover Designer Task Description for a 170 page 6x9 white RVX book.
Title: The Notebook Beneath the Lantern
Author: Colin Marbury
ISBN: 978-1-5318846-9-7
Concept (images are for examples only)
The cover should visually represent the protagonist’s transformation from corporate captivity in Sydney to freedom and reflection in Chiang Mai. The design should feel aspirational, modern, and professional, appealing to readers of personal development, lifestyle design, and narrative nonfiction.
Front Cover Visual Direction
• Left Scene (Sydney):
• A female figure, circa 40years old, in business attire leaving a high‑rise office building at dusk.
• She carries a large office travel bag or briefcase bag.
• The Sydney skyline should be visible in the background, with evening light (purples, oranges, city lights).
• Mood: heavy, corporate, restrained.
• Right Scene (Chiang Mai):
• The same woman, now relaxed, sitting at an outdoor café table in the sunshine.
• She has a coffee in hand, with her journal open on the table.
• Background hints of Chiang Mai: golden temple spire, tropical greenery, warm sunlight.
• Mood: light, free, expansive.
• Design Style:
• A split‑scene composition (left = Sydney evening, right = Chiang Mai morning).
• Title across the centre in bold, modern typography.
• Author name at the bottom.
Back Cover
• Blurb (to include in full):
What if the life you’re living isn’t yours at all?
You followed the rules, climbed the ladder, and earned the perks. But something still feels off. The Sunday dread. The quiet discontent. The whisper that says: This can’t be it.
The Notebook Beneath the Lantern is a raw, reflective journey through corporate captivity, awakening, and the first steps toward freedom. Through the eyes of Maren, a high-performing professional caught in the illusion of security, this book explores what happens when you finally question everything you were told about success, stability, and self-worth.
Blending narrative storytelling with coaching prompts, global lifestyle insights, and real-world case studies, this book offers more than inspiration. It’s a blueprint for change. Whether you’re stuck in the “one more year” loop or quietly dreaming of a different life, this is your invitation to reclaim your time, energy, and direction.
Author Bio:
Colin Marbury is the author of The Tide Nobody Noticed Yet, known for blending creative insight with operational clarity. His work explores the intersection of personal freedom, global mobility, and the systems that shape our choices. Through writing and coaching, he helps readers design lives that are intentional, resilient, and deeply their own.
• ISBN: 978-1-5318846-9-7
• Include barcode space at bottom right.

Target Market(s)

Bored workers between 20-50 looking for a way out of the rat race

Industry/Entity Type

Self help

Colors

Designer to choose colors to be used in the design.

Requirements
Must have
• A worn out woman in her thirties leaving a Sydney office on a grey evening in formal office attire and the same lady dressed casually and happy having a coffee in a café in Chiang Mai with her journal then the same woman
Nice to have
• Temple in the background and maybe a group of young people at other tables looking happy

```html
<!DOCTYPE html>
<html lang="en">
<head>
<meta charset="utf-8">
<title>The Notebook Beneath the Lantern — Cover</title>
<link rel="stylesheet" href="https://fonts.googleapis.com/css2?family=Montserrat:wght@300;400;700&display=swap">
<style>
  :root {
    --navy-top: #0e0a4f;
    --navy-bottom: #3b2b74;
    --spine: #a56ab0;
    --white: #ffffff;
    --dusk-top: #3a2cc0;
    --dusk-mid: #6a4aa8;
    --dusk-low: #e08a5a;
    --sun-top: #f6d9a0;
    --sun-mid: #e9a54e;
    --sun-low: #6e5a2a;
  }
  * { margin: 0; padding: 0; box-sizing: border-box; }
  html, body { width: 1200px; height: 879px; overflow: hidden; background: #fff; }
  body { font-family: 'Montserrat', sans-serif; color: var(--white); }

  .cover { position: relative; width: 1200px; height: 879px; }

  /* Back cover */
  .back {
    position: absolute; left: 0; top: 0; width: 582px; height: 879px;
    background: linear-gradient(180deg, var(--navy-top) 0%, #241a63 45%, var(--navy-bottom) 100%);
  }
  .back-heading {
    position: absolute; left: 0; width: 582px; top: 106px;
    text-align: center; font-weight: 700; font-size: 17px; letter-spacing: 0.4px;
  }
  .rule { position: absolute; height: 4px; background: var(--white); }
  .rule-top { left: 149px; top: 139px; width: 295px; }
  .rule-bottom { left: 147px; top: 516px; width: 296px; }
  .blurb {
    position: absolute; left: 101px; top: 157px; width: 400px;
    font-weight: 700; font-size: 12.4px; line-height: 15.9px; text-transform: uppercase;
    letter-spacing: 0.2px;
  }
  .author-photo { position: absolute; left: 83px; top: 551px; width: 117px; height: 125px; background: var(--white); }
  .bio {
    position: absolute; left: 208px; top: 540px; width: 292px;
    font-weight: 300; font-size: 12.4px; line-height: 15.9px; text-transform: uppercase; letter-spacing: 0.3px;
  }
  .bio strong { font-weight: 700; }
  .barcode-space { position: absolute; left: 363px; top: 747px; width: 181px; height: 100px; background: var(--white); }

  /* Spine */
  .spine {
    position: absolute; left: 582px; top: 0; width: 36px; height: 879px; background: var(--spine);
  }
  .spine-text {
    position: absolute; left: 0; width: 36px; writing-mode: vertical-rl;
    display: flex; align-items: center; justify-content: flex-start;
    font-weight: 300; font-size: 17px; letter-spacing: 0.6px; text-transform: uppercase;
  }
  .spine-title { top: 74px; }
  .spine-author { top: 582px; }

  /* Front cover */
  .front { position: absolute; left: 618px; top: 0; width: 582px; height: 879px; }
  .front-art { position: absolute; inset: 0; }
  .front-title {
    position: absolute; left: 103px; top: 66px; text-transform: uppercase; line-height: 1;
  }
  .title-the { display: block; font-weight: 300; font-size: 38px; letter-spacing: 1px; }
  .title-main { display: block; font-weight: 700; font-size: 58px; letter-spacing: 0.5px; margin-top: 4px; }
  .title-small { font-weight: 300; font-size: 22px; letter-spacing: 0.5px; margin-left: 2px; }
  .title-last { display: block; font-weight: 700; font-size: 44px; letter-spacing: 0.5px; margin-top: 8px; }
  .front-author {
    position: absolute; left: 103px; top: 796px; font-weight: 700; font-size: 38px;
    letter-spacing: 0.5px; text-transform: uppercase; text-shadow: 0 2px 4px rgba(0,0,0,0.45);
  }
</style>
</head>
<body>
<div class="cover">

  <section class="back">
    <h2 class="back-heading">THE NOTEBOOK BENEATH THE LANTERN</h2>
    <div class="rule rule-top"></div>
    <p class="blurb">
      What if the life you’re living isn’t yours at all? You followed the rules, climbed the ladder, and earned the perks. But something still feels off. The Sunday dread. The quiet discontent. The whisper that says: This can’t be it.<br>
      The Notebook Beneath the Lantern is a raw, reflective journey through corporate captivity, awakening, and the first steps toward freedom. Through the eyes of Maren, a high-performing professional caught in the illusion of security, this book explores what happens when you finally question everything you were told about success, stability, and self-worth.<br>
      Blending narrative storytelling with coaching prompts, global lifestyle insights, and real-world case studies, this book offers more than inspiration. It’s a blueprint for change. Whether you’re stuck in the “one more year” loop or quietly dreaming of a different life, this is your invitation to reclaim your time, energy, and direction.
    </p>
    <div class="rule rule-bottom"></div>
    <div class="author-photo" role="img" aria-label="Author photo space"></div>
    <p class="bio">
      <strong>Colin Marbury</strong> is the author of The Tide Nobody Noticed Yet, known for blending creative insight with operational clarity. His work explores the intersection of personal freedom, global mobility, and the systems that shape our choices. Through writing and coaching, he helps readers design lives that are intentional, resilient, and deeply their own.
    </p>
    <div class="barcode-space" aria-label="Barcode space"></div>
  </section>

  <section class="spine">
    <div class="spine-text spine-title">The Notebook Beneath the Lantern</div>
    <div class="spine-text spine-author">Colin Marbury</div>
  </section>

  <section class="front">
    <svg class="front-art" width="582" height="879" viewBox="0 0 582 879" role="img"
         aria-label="Split illustration: a woman in business attire leaving a high-rise office at dusk with the Sydney skyline behind her, and the same woman relaxing at a sunny café table in Chiang Mai with coffee, an open journal, a golden temple spire and palm trees">
      <defs>
        <linearGradient id="duskScene" x1="0" y1="0" x2="0" y2="1">
          <stop offset="0" stop-color="var(--dusk-top)"/>
          <stop offset="0.42" stop-color="var(--dusk-mid)"/>
          <stop offset="0.6" stop-color="var(--dusk-low)"/>
          <stop offset="1" stop-color="#8a6a7a"/>
        </linearGradient>
        <linearGradient id="sunScene" x1="0" y1="0" x2="0" y2="1">
          <stop offset="0" stop-color="#1a1450"/>
          <stop offset="0.3" stop-color="var(--sun-top)"/>
          <stop offset="0.6" stop-color="var(--sun-mid)"/>
          <stop offset="1" stop-color="var(--sun-low)"/>
        </linearGradient>
      </defs>
      <rect x="0" y="0" width="289" height="879" fill="url(#duskScene)"/>
      <rect x="289" y="0" width="293" height="879" fill="url(#sunScene)"/>
    </svg>

    <h1 class="front-title">
      <span class="title-the">The</span>
      <span class="title-main">Notebook<span class="title-small">Beneath</span></span>
      <span class="title-last">The Lantern</span>
    </h1>
    <div class="front-author">Colin Marbury</div>
  </section>

</div>
</body>
</html>
```